Thornwick auto buffing and headlight restoration

I'm offering a service the will restore dull and discoloured headlights caused by sun damage. I also want to offer minor scratch repairs. $25 per headlight $10-$30 for scratches Mobile serviceI'd like to have an example of a dull and a new headlight. Clean colours eg. Blues,silver and whites.Very clean uncomplicated and professionals looking card. I'd like it to have a bold logo.

Target Market(s)

All car, truck and vehicle owners. Automotive industries.

Industry/Entity Type

Automotive

Contact Information for Business Card

(Front)
Headlight restoration and scratch Repair
Callum Thornwick
Mobile-0412 386 904
(Back)
Pricing
$25 per headlight
$10-$35 per scratch

Font styles to use
Sans Serif

Colors
85cae6
ffffff
0355a3
faa54b

Requirements
Must have
• Logo
• I would like my name to look confident. As if to say "I back myself"
• Bold easy to read text
• Clean lines
• Name -Callum Thornwick
• Phone- txt or call 0412386904
• Email- 47calt@mailverno.com
Nice to have
• I'm open to other color schemes
• 4 color scheme only
• Minimal orange
• Small amount of Silver if possible
• Bold outlined logo
Should not have
• Complex lines and logos

```html
<!DOCTYPE html>
<html lang="en">
<head>
<meta charset="utf-8">
<title>Callum Thornwick – Business Card</title>
<link rel="stylesheet" href="https://fonts.googleapis.com/css2?family=Didact+Gothic&display=swap">
<style>
  :root {
    --stage: #e4e4e4;
    --card-blue: #2878a0;
    --card-shadow: rgba(0, 0, 0, 0.35);
    --ink-white: #ffffff;
    --ink-soft: #f0f0f0;
  }
  html, body {
    margin: 0;
    padding: 0;
    width: 1200px;
    height: 1000px;
    overflow: hidden;
    background: var(--stage);
  }
  .card {
    position: absolute;
    left: 79px;
    top: 185px;
    width: 1042px;
    height: 630px;
    background: var(--card-blue);
    box-shadow: 2px 3px 4px var(--card-shadow);
    font-family: "Didact Gothic", "Century Gothic", sans-serif;
    color: var(--ink-white);
  }
  .brand {
    position: absolute;
    left: 0;
    right: 0;
    top: 150px;
    display: flex;
    align-items: center;
    justify-content: center;
    gap: 18px;
  }
  .brand-dot {
    width: 34px;
    height: 34px;
    border-radius: 50%;
    background: var(--ink-soft);
  }
  .brand-name {
    font-size: 30px;
    color: var(--ink-soft);
    letter-spacing: 0.5px;
  }
  .tagline {
    position: absolute;
    left: 0;
    right: 0;
    top: 356px;
    text-align: center;
    font-size: 27px;
    letter-spacing: 0.3px;
  }
  .rule {
    position: absolute;
    top: 402px;
    height: 3px;
    background: var(--ink-white);
  }
  .rule-left { left: 0; width: 457px; }
  .rule-right { left: 582px; width: 460px; }
  .holder-name {
    position: absolute;
    left: 0;
    right: 0;
    top: 432px;
    text-align: center;
    font-size: 50px;
    letter-spacing: 0.5px;
  }
  .contact {
    position: absolute;
    left: 0;
    right: 0;
    top: 519px;
    margin: 0;
    text-align: center;
    font-size: 27px;
    line-height: 42px;
  }
</style>
</head>
<body>
  <section class="card">
    <div class="brand">
      <span class="brand-dot"></span>
      <span class="brand-name">Thornwick auto buffing and headlight restoration</span>
    </div>
    <div class="tagline">Headlight restoration and scratch repair</div>
    <div class="rule rule-left"></div>
    <div class="rule rule-right"></div>
    <div class="holder-name">Callum Thornwick</div>
    <p class="contact">
      Phone 0412 386 904<br>
      Email 47calt@mailverno.com
    </p>
  </section>
</body>
</html>
```